Velvet Lantern rebranding my business with a new business card

I have my new logo and now I need a refresher on my business cards. I really want something fun and fresh. I like black background or anything to make the color pop.
Logo
Name: Velvet Lantern
Contact Info as stated below:
Mara Pelkin
519-555-0147
Logo
Name: Velvet Lantern
Mara Pelkin
519-555-0147
fb.me/VelvetLanternbyMara
Instagram: @VelvetLanternbyMara

Industry/Entity Type

Business

Contact Information for Business Card

double-sided. Logo on one side. Contact info on the other.

Requirements
Must have
• Logo
• Name: Velvet Lantern
• Contact Info as stated below:
• Mara Pelkin
• 519-555-0147
• fb.me/VelvetLanternbyMara
• fb.me/VelvetLanternbyMara

```html
<!DOCTYPE html>
<html lang="en">
<head>
<meta charset="utf-8">
<title>Velvet Lantern — Business Card</title>
<link rel="stylesheet" href="https://fonts.googleapis.com/css2?family=Germania+One&family=Questrial&display=swap">
<style>
  :root {
    --page: #ffffff;
    --card: #ffffff;
    --pattern-a: #f6f2f2;
    --pattern-b: #fbf8f8;
    --brand-red: #d2232a;
    --brand-teal: #3db7a4;
    --logo-pink: #eaa9cb;
    --logo-teal: #7fd6c8;
    --shadow: rgba(0, 0, 0, 0.45);
  }
  * { box-sizing: border-box; margin: 0; padding: 0; }
  html, body {
    width: 1200px; height: 1200px; overflow: hidden;
    background: var(--page);
  }
  .canvas { position: relative; width: 1200px; height: 1200px; }
  .card {
    position: absolute; left: 244px; width: 747px; height: 447px;
    background: var(--card);
    box-shadow: 0 12px 40px var(--shadow);
    overflow: hidden;
  }
  .card--front { top: 95px; }
  .card--back { top: 654px; }
  .card__pattern {
    position: absolute; inset: 0;
    background: linear-gradient(135deg, var(--pattern-a), var(--pattern-b) 50%, var(--pattern-a));
  }
  .logo {
    position: absolute; left: 52px; top: 90px; width: 256px; height: 260px;
    display: flex; flex-direction: column; align-items: center; justify-content: center; gap: 18px;
  }
  .logo__mark {
    width: 150px; height: 150px; border-radius: 50%;
    background: var(--logo-pink);
  }
  .logo__name {
    font-family: "Questrial", sans-serif; font-size: 26px;
    color: var(--brand-red);
  }
  .title {
    position: absolute;
    font-family: "Germania One", serif;
    color: var(--brand-red); text-transform: uppercase; white-space: nowrap;
    line-height: 1;
  }
  .card--front .title { left: 314px; top: 126px; font-size: 52px; }
  .card--back .title { left: 310px; top: 188px; font-size: 60px; }
  .contact {
    position: absolute; left: 415px; top: 242px; list-style: none;
    font-family: "Questrial", sans-serif; font-size: 16px; letter-spacing: 0.3px;
  }
  .contact__item {
    display: flex; align-items: center; gap: 12px; height: 29.6px;
  }
  .contact__icon { width: 16px; height: 16px; flex: none; }
  .contact__icon--square { width: 13px; height: 13px; margin: 0 1.5px; }
  .is-teal { color: var(--brand-teal); }
  .is-red { color: var(--brand-red); }
  .social {
    position: absolute; top: 374px;
    display: flex; align-items: center; gap: 6px;
    font-family: "Questrial", sans-serif; font-size: 16px; white-space: nowrap;
  }
  .social--facebook { left: 54px; }
  .social--instagram { right: 55px; }
  .social__square { width: 12px; height: 12px; }
</style>
</head>
<body>
<main class="canvas">

  <section class="card card--front" aria-label="Card front">
    <div class="card__pattern" role="img" aria-label="Faint repeating cupcake pattern background"></div>
    <div class="logo">
      <div class="logo__mark"></div>
      <span class="logo__name">Velvet Lantern</span>
    </div>
    <h1 class="title">Velvet Lantern</h1>
    <ul class="contact">
      <li class="contact__item is-teal">
        <svg class="contact__icon" viewBox="0 0 16 16" aria-hidden="true"><path d="M8 1.5 1 8h2.2v6.5h3.6V10h2.4v4.5h3.6V8H15z" fill="currentColor"/></svg>
        <span>Mara Pelkin</span>
      </li>
      <li class="contact__item is-red">
        <svg class="contact__icon" viewBox="0 0 16 16" aria-hidden="true"><path d="M3.6 1.2 6 3.8 4.7 5.6c.9 2.2 2.6 3.9 4.8 4.8l1.8-1.3 2.6 2.4-1.4 2.6C6.8 13.9 2.1 9.2 2 3z" fill="currentColor"/></svg>
        <span>519-555-0147</span>
      </li>
      <li class="contact__item is-teal">
        <svg class="contact__icon contact__icon--square" viewBox="0 0 13 13" aria-hidden="true"><rect width="13" height="13" fill="currentColor"/></svg>
        <span>fb.me/VelvetLanternbyMara</span>
      </li>
      <li class="contact__item is-red">
        <svg class="contact__icon contact__icon--square" viewBox="0 0 13 13" aria-hidden="true"><rect width="13" height="13" fill="currentColor"/></svg>
        <span>@VelvetLanternbyMara</span>
      </li>
    </ul>
  </section>

  <section class="card card--back" aria-label="Card back">
    <div class="card__pattern" role="img" aria-label="Faint repeating cupcake pattern background"></div>
    <div class="logo">
      <div class="logo__mark"></div>
      <span class="logo__name">Velvet Lantern</span>
    </div>
    <h2 class="title">Velvet Lantern</h2>
    <p class="social social--facebook is-teal">
      <svg class="social__square" viewBox="0 0 12 12" aria-hidden="true"><rect width="12" height="12" fill="currentColor"/></svg>
      <span>fb.me/VelvetLanternbyMara</span>
    </p>
    <p class="social social--instagram is-red">
      <svg class="social__square" viewBox="0 0 12 12" aria-hidden="true"><rect width="12" height="12" fill="currentColor"/></svg>
      <span>@VelvetLanternbyMara</span>
    </p>
  </section>

</main>
</body>
</html>
```